Engineering group involved with fire safety needs a business card

We need a business card design for a company based in Greece called "Varotis Group". We are engineers and specialized technicians, operating the following : a) Fire fighting equipment trade b) Installation , Inspection & Maintenance of fire extinguishers and fire protection systems c) Occupational Health & Safety (Risk assessment & management/ Staff training). We need a clear and simple card design. I uploaded a draft I made, in order to give you an idea of the company and how I currently imagine the design of the card. I also uploaded the logo in .png file format. We are always open to different, new suggestions and ideas you may want to submit.
Target Market(s)
industries, companies, managers, retail clients
Industry/Entity Type
Fire Safety
Contact Information for Business Card
Addresses & phone numbers (headquarters + branch), logo, name (you can find all the details on the uploaded files!)
Colors
Designer to choose colors to be used in the design.
Look and feel
Each slider illustrates characteristics of the customer's brand and the style your logo design should communicate.

```html
<!DOCTYPE html>
<html lang="en">
<head>
<meta charset="utf-8">
<title>Varotis Group – Business Card</title>
<link href="https://fonts.googleapis.com/css2?family=Poppins:wght@300;400;500;600&display=swap" rel="stylesheet">
<style>
  :root{
    --stage:#262626;
    --paper:#dcdbd9;
    --paper-tint:#bcc3c2;
    --ink:#2b2b2b;
    --charcoal:#1f1f1f;
    --charcoal-light:#2a2b2c;
    --red:#d91c1f;
    --grey:#7f8385;
  }
  *{box-sizing:border-box;margin:0;padding:0}
  html,body{width:1200px;height:960px;overflow:hidden;background:var(--stage)}
  body{font-family:"Poppins",sans-serif;display:flex;flex-direction:column;align-items:center;justify-content:center;gap:36px}
  .card{width:760px;height:434px;border-radius:28px;position:relative;overflow:hidden}

  /* contact side */
  .card--contact{background:var(--paper);color:var(--ink)}
  .card--contact .tint-band{position:absolute;right:0;top:0;width:46%;height:100%;
    background:linear-gradient(180deg,var(--paper-tint),rgba(188,195,194,.55))}
  .person{position:absolute;right:44px;top:40px;text-align:right}
  .person__name{font-size:30px;font-weight:400;letter-spacing:3px;line-height:1.1}
  .person__name .first{color:var(--red)}
  .person__role{font-size:13px;letter-spacing:.6px;margin-top:4px}
  .contacts{position:absolute;right:44px;top:142px;width:560px;font-size:12.5px}
  .contacts__row{display:flex;justify-content:flex-end;gap:22px;margin-bottom:10px}
  .contact{display:flex;align-items:center;gap:7px;white-space:nowrap}
  .contact svg{width:15px;height:15px;flex:none}
  .rule{height:1.5px;background:var(--red);margin:6px 0 12px}
  .address{display:flex;gap:7px;justify-content:flex-end;line-height:1.35}
  .address svg{width:15px;height:15px;margin-top:2px;flex:none}
  .brand-small{position:absolute;left:44px;bottom:40px;display:flex;align-items:center;gap:10px;
    font-size:18px;font-weight:600;color:var(--red);letter-spacing:1px}
  .brand-small .mark{width:16px;height:16px;background:var(--grey)}

  /* brand side */
  .card--brand{background:linear-gradient(120deg,var(--charcoal) 45%,var(--charcoal-light));color:var(--grey);text-align:center}
  .brand{position:absolute;left:0;right:0;top:120px;display:flex;flex-direction:column;align-items:center}
  .brand__name{font-size:44px;font-weight:600;color:var(--red);letter-spacing:4px;line-height:1}
  .brand__dot{width:14px;height:14px;border-radius:50%;background:var(--grey);margin-bottom:18px}
  .services{position:absolute;left:0;right:0;bottom:74px}
  .services__main{font-size:26px;font-weight:400;letter-spacing:.5px}
  .services__main .accent{color:var(--red)}
  .services__sub{font-size:10.5px;letter-spacing:1px;line-height:1.5;margin-top:6px;text-transform:uppercase}
</style>
</head>
<body>

<section class="card card--contact">
  <div class="tint-band"></div>
  <div class="person">
    <h1 class="person__name"><span class="first">STAVROS</span> VAROTIS</h1>
    <p class="person__role">Mechanical Engineer-OHS Consultant</p>
  </div>
  <div class="contacts">
    <div class="contacts__row">
      <span class="contact"><svg viewBox="0 0 16 16"><circle cx="8" cy="8" r="8" fill="#d91c1f"/><path d="M5 4.5l1.6-.3.9 2-1 .8a5 5 0 002.5 2.5l.8-1 2 .9-.3 1.6c-3.6.3-6.8-2.9-6.5-6.5z" fill="#fff"/></svg>(HQ)+30 22910 45120</span>
      <span class="contact"><svg viewBox="0 0 16 16"><circle cx="8" cy="8" r="8" fill="#d91c1f"/><path d="M5 4.5l1.6-.3.9 2-1 .8a5 5 0 002.5 2.5l.8-1 2 .9-.3 1.6c-3.6.3-6.8-2.9-6.5-6.5z" fill="#fff"/></svg>(BO)+30 210 6142790</span>
      <span class="contact"><svg viewBox="0 0 16 16"><circle cx="8" cy="8" r="8" fill="#d91c1f"/><path d="M5 4.5l1.6-.3.9 2-1 .8a5 5 0 002.5 2.5l.8-1 2 .9-.3 1.6c-3.6.3-6.8-2.9-6.5-6.5z" fill="#fff"/></svg>+30 694 512 37 80</span>
    </div>
    <div class="contacts__row">
      <span class="contact"><svg viewBox="0 0 16 16"><circle cx="8" cy="8" r="8" fill="#d91c1f"/><circle cx="8" cy="8" r="4" fill="none" stroke="#fff" stroke-width="1"/><path d="M4 8h8M8 4c-2 2.5-2 5.5 0 8M8 4c2 2.5 2 5.5 0 8" fill="none" stroke="#fff" stroke-width=".8"/></svg>www.varotisgroup.gr</span>
      <span class="contact"><svg viewBox="0 0 16 16"><circle cx="8" cy="8" r="8" fill="#d91c1f"/><rect x="4" y="5" width="8" height="6" fill="none" stroke="#fff" stroke-width="1"/><path d="M4 5l4 3.5L12 5" fill="none" stroke="#fff" stroke-width="1"/></svg>info@varotisgroup.gr</span>
    </div>
    <div class="rule"></div>
    <div class="address">
      <svg viewBox="0 0 16 16"><circle cx="8" cy="8" r="8" fill="#d91c1f"/><path d="M8 12.5s-3-3-3-5.2a3 3 0 016 0c0 2.2-3 5.2-3 5.2z" fill="#fff"/><circle cx="8" cy="7.2" r="1.1" fill="#d91c1f"/></svg>
      <p>headquarters: 12 Agiou Nikolaou, 19400 Koropi<br>Branch Office: 18 Ermou Street, 15231 Chalandri</p>
    </div>
  </div>
  <div class="brand-small"><span class="mark"></span>Varotis Group</div>
</section>

<section class="card card--brand">
  <div class="brand">
    <span class="brand__dot"></span>
    <p class="brand__name">VAROTIS GROUP</p>
  </div>
  <div class="services">
    <p class="services__main">installation-<span class="accent">inspection</span>-maintenance</p>
    <p class="services__sub">Fire fighting equipment licencing &amp; business registration<br>Occupational health &amp; safety staff training</p>
  </div>
</section>

</body>
</html>
```